RT Appraisals website redesign

I would like to refresh my existing website of www.rtappraisals.example with new graphics, look and feel, as well as updated structure and wording. Content and layout changes have been uploaded to this project Brief.

My existing website has a dark feel. I am now looking for a light and energetic feel. Financial Services is my industry, so the website should be reflect that. I would also like to reflect the concepts of Trust, Service and Expertise.

The website must be serious and upmarket.

Target Market(s)

Corporate board members, CFO's, treasurers and controllers
Auditors, tax advisors, private equity and venture capital asset managers, investors, tax authorities

Industry/Entity Type

Financial Service

Coding

Coded - Design and coding required

Number of Pages Required

5+ page

Font styles to use
Sans Serif
Other font styles liked:
• Designer can choose another modern font

Colors
0355a3
3277b5
85acd3
eaf1f7
f37122
f68d4d
9bcb3c
acd037
cadf82

Requirements
Must have
• Good hi resolution pictures that convey "Finance", "Trust", "Service" or "Expertise".
• An anti-bot (such as Captcha) mechanism in the contact form.
Should not have
• Must not have all content on one rolling screen.

```html
<!DOCTYPE html>
<html lang="en">
<head>
<meta charset="utf-8">
<title>RT Appraisals – Business and Intellectual Property Valuation</title>
<link rel="stylesheet" href="https://fonts.googleapis.com/css2?family=Mulish:wght@400;600;700;800;900&display=swap">
<style>
:root{
  --violet:#6a5cf0;
  --indigo:#3d1fe6;
  --sky:#5a8ee8;
  --orange:#f68d4d;
  --orange-deep:#f37122;
  --blue:#1f6bb2;
  --blue-bright:#2f8ef0;
  --blue-text:#2266b4;
  --ink:#1c1c22;
  --body:#4a4a52;
  --mist:#e9eff7;
  --ghost:#efeff1;
  --paper:#fafafb;
  --white:#ffffff;
}
*{margin:0;padding:0;box-sizing:border-box}
html,body{width:1200px;height:2567px;overflow:hidden;background:var(--white)}
body{font-family:"Mulish",sans-serif;color:var(--ink)}
.page{position:relative;width:1200px;height:2567px;overflow:hidden}
.abs{position:absolute}

/* hero */
.hero-bg{left:0;top:0}
.brand{left:267px;top:38px;font-size:17px;font-weight:600;color:var(--white);letter-spacing:.5px;display:flex;align-items:center;gap:8px}
.brand-mark{width:12px;height:12px;border:2px solid var(--white)}
.nav{left:560px;top:43px;display:flex;gap:28px;font-size:10px;font-weight:700;color:var(--white)}
.hero-title{left:264px;top:140px;font-size:34px;font-weight:600;line-height:42px;color:var(--white)}
.hero-sub{left:267px;top:231px;font-size:10px;color:var(--white)}
.ghost-word{left:120px;top:256px;font-size:118px;font-weight:900;color:rgba(255,255,255,.08);letter-spacing:2px;white-space:nowrap}
.btn{display:flex;align-items:center;justify-content:center;gap:10px;color:var(--white);font-size:12px;font-weight:700}
.btn-orange{background:var(--orange)}
.hero-btn{left:267px;top:261px;width:142px;height:32px}
.hero-photo{left:0;top:363px;width:878px;height:407px;background:linear-gradient(120deg,#e9ecef 0%,#cfd2d4 35%,#b8924a 60%,#8c6a30 80%,#d8c9a8 100%)}
.slide-arrow{top:736px;width:48px;height:25px;background:var(--blue-bright);display:flex;align-items:center;justify-content:center}

/* pillars */
.rule{left:152px;top:883px;width:113px;height:2px;background:var(--ink)}
.pillars-title{left:280px;top:870px;font-size:20px;font-weight:600;line-height:27px}
.card{border:2px solid var(--ink);background:var(--white)}
.card h3{position:absolute;font-size:20px;font-weight:600}
.card p{position:absolute;font-size:10.5px;line-height:14.5px;color:var(--body)}
.card svg{position:absolute}
.num{font-size:82px;font-weight:800;color:var(--ghost);background:var(--white);line-height:80px;width:42px;text-align:center}

/* services */
.services-bg{left:0;top:1195px}
.services-word{left:716px;top:1270px;font-size:96px;font-weight:900;color:#ebebed;letter-spacing:-2px}
.services-lead{left:103px;top:1470px;font-size:19px;font-weight:600;line-height:26px}
.services-lead span{color:var(--blue-text)}
.services-btn{left:105px;top:1538px;width:164px;height:28px}
.service-photo{top:1358px;height:352px}
.service-label{top:1632px;width:165px;height:64px;background:var(--white);display:flex;align-items:center;padding-left:16px;font-size:14px;font-weight:600;line-height:20px}
.circle-btn{top:1734px;width:28px;height:28px;border:1.5px solid var(--ink);border-radius:50%;display:flex;align-items:center;justify-content:center}

/* testimonial */
.testimonial{left:0;top:1812px;width:1200px;height:265px;background:var(--mist)}
.testimonial-title{left:267px;top:1881px;font-size:21px;font-weight:600;line-height:23px;color:#2a2a30}
.testimonial-link{left:269px;top:1963px;font-size:12px;font-weight:700;color:var(--blue-text);border-bottom:1.5px solid var(--blue-text);padding:0 1px 2px}
.quote{left:543px;top:1883px;width:358px;font-size:10.5px;line-height:14.5px;color:var(--body)}
.author{left:543px;top:1990px;font-size:12px;font-weight:700;color:#2a2a30}

/* contact */
.cta-title{left:0;top:2165px;width:1200px;text-align:center;font-size:20px;font-weight:600}
.cta-btn{left:522px;top:2208px;width:158px;height:32px;background:var(--blue);border-radius:16px}
.footer-bg{left:0;top:0}
.footer-links{left:0;top:2434px;width:1200px;display:flex;justify-content:center;gap:12px;font-size:10px;color:var(--white)}
.copyright{left:0;top:2458px;width:1200px;text-align:center;font-size:10px;color:var(--white)}
</style>
</head>
<body>
<div class="page">

  <!-- hero -->
  <svg class="abs hero-bg" width="1200" height="600" viewBox="0 0 1200 600">
    <defs>
      <linearGradient id="heroGrad" x1="0" y1="1" x2="1" y2="0">
        <stop offset="0" stop-color="#4f9be6"/>
        <stop offset=".35" stop-color="#6b63ee"/>
        <stop offset=".75" stop-color="#5a3fe9"/>
        <stop offset="1" stop-color="#3416e2"/>
      </linearGradient>
    </defs>
    <path d="M0 0H1200V355C1090 385 1030 470 960 540C935 565 905 585 870 595H0Z" fill="url(#heroGrad)"/>
  </svg>

  <div class="abs brand"><span class="brand-mark"></span>RT APPRAISALS</div>
  <nav class="abs nav"><span>Home</span><span>About Us</span><span>Our Services</span><span>News &amp; Views</span><span>Contact Us</span></nav>
  <div class="abs ghost-word">RT APPRAISALS</div>
  <h1 class="abs hero-title">Business and Intellectual<br>Property Valuation</h1>
  <p class="abs hero-sub">RT Appraisals is a corporate finance companies throughout Europe and North America.</p>
  <a class="abs btn btn-orange hero-btn">Contact Us
    <svg width="30" height="10" viewBox="0 0 30 10"><path d="M0 5H28M23 1L28 5L23 9" fill="none" stroke="#fff" stroke-width="1.3"/></svg></a>

  <div class="abs hero-photo" role="img" aria-label="Photo of stacked gold coins on financial newspaper pages"></div>
  <div class="abs slide-arrow" style="left:769px"><svg width="20" height="10" viewBox="0 0 20 10"><path d="M20 5H2M6 1L2 5L6 9" fill="none" stroke="#fff" stroke-width="1.3"/></svg></div>
  <div class="abs slide-arrow" style="left:822px"><svg width="20" height="10" viewBox="0 0 20 10"><path d="M0 5H18M14 1L18 5L14 9" fill="none" stroke="#fff" stroke-width="1.3"/></svg></div>

  <!-- pillars -->
  <div class="abs rule"></div>
  <h2 class="abs pillars-title">Trust, Service and Expertise<br>are the 3 pillars of RT Appraisals.</h2>

  <div class="abs card" style="left:283px;top:976px;width:195px;height:192px">
    <svg style="left:29px;top:15px" width="28" height="32" viewBox="0 0 28 32"><path d="M14 2L25 6V15C25 22 20 27 14 30C8 27 3 22 3 15V6Z" fill="none" stroke="#1c1c22" stroke-width="1.6"/><path d="M9 16L13 20L20 12" fill="none" stroke="#1c1c22" stroke-width="1.6"/></svg>
    <h3 style="left:30px;top:55px">Trust</h3>
    <p style="left:31px;top:90px;width:142px">Trust is paramount. Clients rely on RT Appraisals for confidentiality, transparency and independence.</p>
  </div>
  <div class="abs num" style="left:255px;top:1060px">1</div>

  <div class="abs card" style="left:510px;top:975px;width:196px;height:193px">
    <svg style="left:48px;top:17px" width="28" height="30" viewBox="0 0 28 30"><rect x="2" y="2" width="22" height="26" fill="none" stroke="#1c1c22" stroke-width="1.5"/><path d="M2 8H24" stroke="#1c1c22" stroke-width="1.5"/><rect x="6" y="12" width="5" height="5" fill="none" stroke="#1c1c22" stroke-width="1.3"/><path d="M14 14H20M6 21H11M14 22H20" stroke="#1c1c22" stroke-width="1.3"/><path d="M7 14L9 16L12 11" fill="none" stroke="#1c1c22" stroke-width="1.2"/></svg>
    <h3 style="left:47px;top:55px">Service</h3>
    <p style="left:47px;top:87px;width:130px">Service is front and center at RT Appraisals. We consider the needs of all stakeholders and the personal needs of the client team involved.</p>
  </div>
  <div class="abs num" style="left:488px;top:1060px">2</div>

  <div class="abs card" style="left:740px;top:902px;width:196px;height:268px">
    <svg style="left:28px;top:26px" width="36" height="36" viewBox="0 0 36 36"><path d="M8 33V26C4 23 2 19 3 14C5 6 12 2 19 3C27 4 32 11 31 18L33 22H30V27C30 29 28 30 26 30H22V33" fill="none" stroke="#1c1c22" stroke-width="1.5"/><circle cx="19" cy="14" r="3" fill="none" stroke="#1c1c22" stroke-width="1.4"/><circle cx="19" cy="14" r="6.5" fill="none" stroke="#1c1c22" stroke-width="1.4" stroke-dasharray="3 2"/></svg>
    <h3 style="left:33px;top:68px">Expertise</h3>
    <p style="left:35px;top:97px;width:142px">Expertise is core to the philosophy of RT Appraisals. Our global network of professionals maintain and continue to develop the knowledge and experience that you expect from your trusted corporate finance partner.</p>
  </div>
  <div class="abs num" style="left:712px;top:1058px">3</div>

  <!-- services -->
  <svg class="abs services-bg" width="1200" height="617" viewBox="0 0 1200 617">
    <path d="M0 60C120 30 250 40 380 70C520 100 650 120 800 60C950 0 1100 -5 1200 10V617H0Z" fill="var(--paper)"/>
  </svg>
  <div class="abs services-word">SERVICES</div>
  <h2 class="abs services-lead">Basically we provide 5 main<br>services at <span>RT Appraisals</span></h2>
  <a class="abs btn btn-orange services-btn">View all services
    <svg width="30" height="10" viewBox="0 0 30 10"><path d="M0 5H28M23 1L28 5L23 9" fill="none" stroke="#fff" stroke-width="1.3"/></svg></a>

  <div class="abs service-photo" style="left:415px;width:255px;background:linear-gradient(135deg,#dfe6ef,#c9d7e8 50%,#7fa3d4)" role="img" aria-label="Photo of hands reviewing printed financial bar charts"></div>
  <div class="abs service-photo" style="left:683px;width:255px;background:linear-gradient(135deg,#b7c4d6,#d9d2c8 50%,#a58a70)" role="img" aria-label="Photo of a person signing documents at a desk"></div>
  <div class="abs service-photo" style="left:949px;width:251px;background:linear-gradient(180deg,#5a7fc0,#2e3f7a 60%,#6b5a8e)" role="img" aria-label="Photo of two business people shaking hands by a city window"></div>
  <div class="abs service-label" style="left:432px">Business Valuation</div>
  <div class="abs service-label" style="left:698px;padding-left:15px">Intellectual Property<br>Valuation</div>
  <div class="abs service-label" style="left:966px">M&amp;A Advisory</div>
  <div class="abs circle-btn" style="left:414px"><svg width="8" height="12" viewBox="0 0 8 12"><path d="M6 1L1 6L6 11" fill="none" stroke="#1c1c22" stroke-width="1.4"/></svg></div>
  <div class="abs circle-btn" style="left:450px"><svg width="8" height="12" viewBox="0 0 8 12"><path d="M2 1L7 6L2 11" fill="none" stroke="#1c1c22" stroke-width="1.4"/></svg></div>

  <!-- testimonial -->
  <section class="abs testimonial"></section>
  <h2 class="abs testimonial-title">See what some<br>other clients have to<br>say about RT Appraisals</h2>
  <a class="abs testimonial-link">Client Testimonials</a>
  <p class="abs quote">Now the races of these two have been for some ages utterly extinct, and this is Draftline's version of Lorem Ipsum. Proin gravida nibh vel velit auctor aliquet. Aenean sollicitudin, lorem quis bibendum auctor, nisi elit consequat ipsum, nec sagittis sem nibh id elit. Nam nec llusimperdiet nisi. Proin condimentum fermentum nunc. Etiam pharetra, them would not be at all to my purpose.</p>
  <p class="abs author">- Mira Dalton</p>

  <!-- contact -->
  <h2 class="abs cta-title">Do not hesitate, to contact with us for better help and services.</h2>
  <a class="abs btn cta-btn">Contact Us
    <svg width="32" height="10" viewBox="0 0 32 10"><path d="M0 5H30M25 1L30 5L25 9" fill="none" stroke="#fff" stroke-width="1.3"/></svg></a>

  <svg class="abs footer-bg" width="1200" height="2567" viewBox="0 0 1200 2567" style="pointer-events:none">
    <path d="M0 2258C120 2350 260 2395 420 2385C600 2372 720 2310 880 2305C1020 2300 1130 2350 1200 2410V2567H0Z" fill="var(--blue)"/>
  </svg>
  <nav class="abs footer-links"><span>Home</span><span>|</span><span>About</span><span>|</span><span>Services</span><span>|</span><span>News &amp; Views</span><span>|</span><span>Contact</span></nav>
  <p class="abs copyright">Copyright © 2019 RT Appraisals. All Rights Reserved</p>

</div>
</body>
</html>
```